Workbook Cover Design

I am needing the cover for a workbook designed. I have attached a sample cover along with a few images giving an idea what at I am looking for. I'm open to new color schemes. I also attached a flyer of the event to give you an idea of the current color theme. The workbook will be approximately 8.5 x 11.

Title : Fellowship Workshop 202
Lorna Tebbit Ministries

On the cover I would like to have four sections with the following title under each section:
Evangelism (use photo similar to hands with cross)
Praying in Tongues (Photo similar to bird with heart or one with a mouth speaking)
Authority of the Believer (Photo with badge or similar)
Healing (Photo of man and wheelchair or similar)

Using silhouettes are okay, but I prefer not to have any actual faces of people.

```html
<!DOCTYPE html>
<html lang="en">
<head>
<meta charset="utf-8">
<title>Fellowship Workshop 202 – Workbook Cover</title>
<link rel="stylesheet" href="https://fonts.googleapis.com/css2?family=Anton&family=Yellowtail&family=Federo&display=swap">
<style>
  :root {
    --stage: #232323;
    --paper: #f4f4f4;
    --paper-shade: #dcdcdc;
    --gold: #c9962e;
    --gold-light: #f1d483;
    --gold-dark: #8a5d14;
    --purple: #5b1f8a;
    --purple-dark: #2c0c47;
    --navy: #0d1c44;
    --navy-deep: #0a1124;
    --ink: #141414;
    --label-bg: #0f1d3a;
    --label-text: #f3efe6;
  }
  html, body {
    margin: 0;
    width: 720px;
    height: 1200px;
    overflow: hidden;
    background: var(--stage);
  }
  .cover {
    position: absolute;
    left: 0;
    top: 131px;
    width: 720px;
    height: 938px;
    overflow: hidden;
    background: linear-gradient(160deg, #ffffff 0%, var(--paper) 45%, var(--paper-shade) 100%);
  }
  .cover__navy {
    position: absolute;
    left: 0; right: 0; top: 420px; bottom: 0;
    background: linear-gradient(180deg, var(--navy) 0%, var(--navy-deep) 100%);
  }
  .cover__frame {
    position: absolute;
    left: 28px; top: 440px;
    width: 662px; height: 468px;
    background: #ffffff;
  }
  .tile {
    position: absolute;
    overflow: hidden;
  }
  .tile--tongues   { left: 37px;  top: 440px; width: 312px; height: 265px;
    background: radial-gradient(circle at 45% 60%, #f28a2a 0%, #b5320c 35%, #1a0804 75%); }
  .tile--healing   { left: 363px; top: 440px; width: 315px; height: 265px;
    background: linear-gradient(180deg, #6b3a22 0%, #c9662a 50%, #f6b44a 75%, #7a3a18 100%); }
  .tile--evangelism{ left: 37px;  top: 713px; width: 312px; height: 187px;
    background: radial-gradient(circle at 50% 55%, #fff6d8 0%, #f0b25a 22%, #9fb4bd 60%, #6f8c99 100%); }
  .tile--authority { left: 363px; top: 713px; width: 315px; height: 187px;
    background: linear-gradient(180deg, #3c1660 0%, var(--purple-dark) 100%); }
  .tile__label {
    position: absolute;
    left: 50%;
    transform: translateX(-50%);
    bottom: 10px;
    width: 228px;
    height: 31px;
    background: var(--label-bg);
    color: var(--label-text);
    font-family: "Federo", serif;
    font-size: 19px;
    line-height: 31px;
    text-align: center;
    white-space: nowrap;
  }
  .tile--authority .tile__label { bottom: 12px; width: 226px; }
  .badge-shape {
    position: absolute;
    left: 50%; top: 20px;
    width: 88px; height: 104px;
    transform: translateX(-50%);
    background: linear-gradient(160deg, var(--gold-light), var(--gold) 55%, var(--gold-dark));
    border-radius: 40% 40% 45% 45%;
  }
  .wave, .masthead {
    position: absolute;
    left: 0; top: 0;
  }
  .ministry-name {
    position: absolute;
    left: 0; right: 0; top: 48px;
    margin: 0;
    text-align: center;
    font-family: "Federo", serif;
    font-weight: 400;
    font-size: 44px;
    line-height: 54px;
    color: var(--ink);
    letter-spacing: 1px;
  }
  .cover__bottom {
    position: absolute;
    left: 0; right: 0; top: 908px; bottom: 0;
    background: var(--navy-deep);
  }
</style>
</head>
<body>
<main class="cover">
  <div class="cover__navy"></div>
  <div class="cover__frame"></div>

  <section class="tile tile--tongues" role="img" aria-label="Photo of a flaming heart with a white dove in flight">
    <div class="tile__label">Praying in Tongues</div>
  </section>
  <section class="tile tile--healing" role="img" aria-label="Silhouette of a person raising arms beside an empty wheelchair at sunset">
    <div class="tile__label">Healing</div>
  </section>
  <section class="tile tile--evangelism" role="img" aria-label="Silhouetted open hands lifted toward a glowing cross in the sky">
    <div class="tile__label">Evangelism</div>
  </section>
  <section class="tile tile--authority">
    <div class="badge-shape" role="img" aria-label="Gold officer badge"></div>
    <div class="tile__label">Authority of the Believer</div>
  </section>

  <div class="cover__bottom"></div>

  <svg class="wave" width="720" height="938" viewBox="0 0 720 938" aria-hidden="true">
    <defs>
      <linearGradient id="goldStroke" x1="0" x2="1">
        <stop offset="0" stop-color="#a8741c"/>
        <stop offset="0.5" stop-color="#f0cf7a"/>
        <stop offset="1" stop-color="#b88424"/>
      </linearGradient>
      <linearGradient id="paperFill" x1="0" y1="0" x2="1" y2="1">
        <stop offset="0" stop-color="#ffffff"/>
        <stop offset="0.6" stop-color="#f2f2f2"/>
        <stop offset="1" stop-color="#e2e2e2"/>
      </linearGradient>
    </defs>
    <path d="M0,0 H720 V405 C650,470 560,540 440,522 C300,500 160,450 0,530 Z" fill="url(#paperFill)"/>
    <path d="M0,530 C160,450 300,500 440,522 C560,540 650,470 720,405"
          fill="none" stroke="url(#goldStroke)" stroke-width="9"/>
  </svg>

  <h1 class="ministry-name">Lorna Tebbit<br>Ministries</h1>

  <svg class="masthead" width="720" height="560" viewBox="0 0 720 560" role="img" aria-label="Fellowship Workshop 202">
    <defs>
      <linearGradient id="goldText" x1="0" y1="0" x2="0" y2="1">
        <stop offset="0" stop-color="#f3d98a"/>
        <stop offset="0.5" stop-color="#c9962e"/>
        <stop offset="1" stop-color="#8a5d14"/>
      </linearGradient>
      <linearGradient id="purpleText" x1="0" y1="0" x2="0" y2="1">
        <stop offset="0" stop-color="#8a47c2"/>
        <stop offset="0.5" stop-color="#5b1f8a"/>
        <stop offset="1" stop-color="#2c0c47"/>
      </linearGradient>
    </defs>
    <text x="354" y="282" text-anchor="middle" textLength="570" lengthAdjust="spacingAndGlyphs"
          font-family="Yellowtail, cursive" font-size="140" fill="url(#goldText)">Fellowship</text>
    <text x="350" y="386" text-anchor="middle" textLength="560" lengthAdjust="spacingAndGlyphs"
          font-family="Anton, sans-serif" font-size="130" fill="url(#purpleText)"
          stroke="#1e0830" stroke-width="3" paint-order="stroke">WORKSHOP 202</text>
  </svg>
</main>
</body>
</html>
```